Corporate Web Redesign Project - coded

We would like redesign/refresh of our current site that would allow us to increase the depth of content and create a high quality impression for visitors.

Current site - http://corvanisystems.com/

A previous web redesign project has improved our site but it has not really reached the level we require.

Our customers are global, blue chip, organisations and a professional, corporate style of site is required.

Please note we would prefer a coded website to a just a design. We are happy to provide a zip of our current site if required.
Updates

                                   

Target Market(s)

Global oil and gas producers, KR, Tamberline, Orvadex etc.

Industry/Entity Type

It Professional

Requirements
Must have
• Design should support the level of content we currently have in the existing sitemap - although it should be expandable a site design for a large / complex site would not be appropriate

All current content / pages to be reflected in design

Must be visually appealing

Intuitive and clear navigation that is expandable

Display a high level of professionalism

Use a consistent palette of colours that complements our logo

Clean and organized layout

A way to capture visitor’s information or Call to action (i.e. contact link or form) on every page

Prominent Contact Information
Should not have
• Flash

```html
<!DOCTYPE html>
<html lang="en">
<head>
<meta charset="utf-8">
<title>Corvani Systems</title>
<link rel="stylesheet" href="https://fonts.googleapis.com/css2?family=Open+Sans:wght@400;600;700&family=Arimo:wght@400;700&display=swap">
<style>
:root{
  --page:#f1f2f3;
  --strip:#b7b9bb;
  --teal:#1f4f55;
  --ink:#222;
  --muted:#555;
  --nav-text:#7a7d80;
  --panel:#ffffff;
  --line:#d5d7d9;
  --tile-head:#2b2d2f;
  --accent:#7fd3d0;
  --btn-grey:#a6a8aa;
}
*{box-sizing:border-box;margin:0;padding:0}
html,body{width:897px;height:1200px;overflow:hidden}
body{position:relative;background:var(--page);font-family:"Arimo",Arial,sans-serif;color:var(--ink)}
.abs{position:absolute}
.top-strip{left:96px;top:0;width:703px;height:5px;background:var(--strip)}
.bottom-strip{left:96px;top:1194px;width:703px;height:6px;background:var(--strip)}

.brand{left:98px;top:30px;display:flex;align-items:center;gap:10px}
.brand-mark{width:36px;height:36px;border-radius:50%;background:var(--teal)}
.brand-name{font-family:"Open Sans",sans-serif;font-weight:600;font-size:24px;color:var(--teal);letter-spacing:.5px}
.enquiries{right:98px;top:34px;text-align:right;font-family:"Open Sans",sans-serif;font-size:12.5px;color:var(--muted);line-height:18px}
.enquiries a{color:var(--teal);text-decoration:none;font-size:13px}

.navbar{left:0;top:104px;width:897px;height:32px;background:linear-gradient(#fafafa,#e3e4e5);border-top:1px solid #d2d3d4;border-bottom:1px solid #cfd0d1}
.nav{left:96px;top:104px;height:32px;display:flex;font-family:"Open Sans",sans-serif;font-size:13px;list-style:none}
.nav li{padding:0 16px;line-height:32px;color:var(--nav-text);border-right:1px solid #d2d3d4}
.nav li.current{background:#dcdedf;color:#3d5f66;border-left:1px solid #c6c8c9}

.hero{left:0;top:136px;width:897px;height:256px;background:linear-gradient(180deg,#3b76c4 0%,#6c92cf 38%,#b98cb4 55%,#35476a 72%,#1a2535 100%)}
.hero-title{left:410px;top:206px;font-family:"Open Sans",sans-serif;font-weight:700;font-size:21px;color:#fff}
.hero-points{left:412px;top:244px;list-style:none;font-family:"Open Sans",sans-serif;font-size:12.5px;color:#fff;line-height:19px}
.hero-points li::before{content:"";display:inline-block;width:6px;height:6px;background:#fff;margin-right:8px;vertical-align:2px}
.hero-arrow{top:264px}
.hero-dots{left:428px;top:380px;display:flex;gap:4px}
.hero-dots span{width:6px;height:6px;background:#fff}

.services{left:96px;top:408px;width:703px;height:230px;background:var(--panel);border:1px solid var(--line)}
.section-title{font-family:"Arimo",sans-serif;font-size:20px;font-weight:400;color:var(--teal);text-align:center}
.services .section-title{position:absolute;left:0;right:0;top:10px}
.tiles{position:absolute;left:8px;top:41px;display:flex;gap:1px}
.tile{position:relative;width:171px;height:170px;overflow:hidden}
.tile-head{height:53px;background:var(--tile-head);color:var(--accent);font-family:"Arimo",sans-serif;font-size:15px;text-align:center;display:flex;align-items:center;justify-content:center;line-height:18px;padding:0 6px}
.tile-img{height:117px}
.tile.featured{background:linear-gradient(#8a8c8e,#b0b2b4)}
.tile.featured .tile-head{background:transparent;color:#fff;height:64px}
.read-more{position:absolute;left:14px;top:123px;width:140px;height:36px;background:var(--teal);border:1px solid var(--accent);color:#fff;font-size:12.5px;display:flex;align-items:center;justify-content:center}

.partners .section-title{position:absolute;left:96px;width:703px;top:652px}
.partner-row{left:115px;top:690px;width:665px;display:flex;justify-content:space-between;align-items:center}
.partner{display:flex;align-items:center;gap:5px;font-family:"Arimo",sans-serif;font-size:12px;font-weight:700;color:#5b6066}
.partner i{width:12px;height:12px;background:#9aa0a6;display:block}
.partner i.round{border-radius:50%}

.info{left:96px;top:735px;width:703px;height:258px;background:var(--panel);border:1px solid var(--line)}
.col{position:absolute;top:18px;width:198px;font-size:8.8px;line-height:12.6px;color:#222}
.col h2{font-size:16px;line-height:20px;font-weight:700;color:#444;margin-bottom:16px}
.col p{margin-bottom:8px}
.col strong{font-weight:700}
.col-about{left:27px}
.col-news{left:260px}
.col-location{left:492px;width:190px;line-height:11.2px}
.col-location p{margin-bottom:0}
.col-location p+p{margin-top:10px}
.continue{position:absolute;top:210px;width:90px;height:22px;border:1px solid #bbb;background:linear-gradient(#fff,#e6e6e6);font-size:8.5px;color:#555;display:flex;align-items:center;justify-content:center}

.partner-badge{left:96px;top:1010px;width:335px;height:56px;background:var(--teal);color:#fff;text-align:center;font-family:"Open Sans",sans-serif}
.partner-badge b{display:block;font-size:16px;font-weight:600;margin-top:13px}
.partner-badge small{font-size:7px;display:block}
.touch{left:96px;top:1080px;width:335px;height:52px;background:var(--btn-grey)}
.touch-pill{position:absolute;left:49px;top:8px;width:234px;height:36px;border:2px solid #fff;border-radius:8px;display:flex;align-items:center;justify-content:center;gap:10px;color:#fff;font-family:"Open Sans",sans-serif;font-weight:600;font-size:19px}

.contact-form{left:447px;top:1010px;width:352px;height:122px;background:var(--panel);border:1px solid var(--line)}
.field{position:absolute;height:17px;border:1px solid #999;background:#fff;font-size:9px;color:#444;padding:2px 5px}
.send{position:absolute;left:252px;top:73px;width:76px;height:27px;background:var(--teal);color:#fff;font-size:12px;font-weight:700;display:flex;align-items:center;justify-content:center}

.footer-nav{left:97px;top:1153px;display:flex;gap:8px;list-style:none;font-size:9px;color:#333}
.footer-nav li+li::before{content:"/";margin-right:8px}
.copyright{left:97px;top:1170px;font-size:9px;color:#333}
.social{top:1156px;width:23px;height:23px;border:1px solid #bbb;background:linear-gradient(#fff,#e4e4e4)}
</style>
</head>
<body>
<div class="abs top-strip"></div>

<header>
  <div class="abs brand"><span class="brand-mark"></span><span class="brand-name">Corvani Systems</span></div>
  <div class="abs enquiries">For general enquiries contact<br><a href="#">Enquiries@corvanisystems.com</a></div>
</header>

<div class="abs navbar"></div>
<ul class="abs nav">
  <li class="current">HOME</li><li>NEWS</li><li>ABOUT US</li><li>SOLUTIONS</li><li>CONTACT US</li>
</ul>

<section class="abs hero" role="img" aria-label="Refinery lit at dusk beside a river under a pink and blue sky"></section>
<h1 class="abs hero-title">The Business of Drilling Wells</h1>
<ul class="abs hero-points">
  <li>Understand and communicate project cost and risk</li>
  <li>Control and reduce expenditure</li>
  <li>Learn and improve performance</li>
</ul>
<svg class="abs hero-arrow" style="left:70px" width="12" height="16" viewBox="0 0 12 16"><path d="M10 1 3 8l7 7" fill="none" stroke="#fff" stroke-width="3"/></svg>
<svg class="abs hero-arrow" style="left:815px" width="12" height="16" viewBox="0 0 12 16"><path d="M2 1l7 7-7 7" fill="none" stroke="#fff" stroke-width="3"/></svg>
<div class="abs hero-dots"><span></span><span></span><span></span><span></span></div>

<section class="abs services">
  <h2 class="section-title">Our Services</h2>
  <div class="tiles">
    <div class="tile featured">
      <div class="tile-head">Time &amp; Cost<br>Estimation</div>
      <div class="read-more">Read More</div>
    </div>
    <div class="tile">
      <div class="tile-head">Materials &amp; Cost<br>Control</div>
      <div class="tile-img" role="img" aria-label="Hands holding floating business charts" style="background:linear-gradient(135deg,#1d2a2a,#3e5f5a 60%,#1a2424)"></div>
    </div>
    <div class="tile">
      <div class="tile-head">Lessons Learned</div>
      <div class="tile-img" role="img" aria-label="Word cloud about learning and development" style="background:linear-gradient(135deg,#f4f4f4,#d9d9d9)"></div>
    </div>
    <div class="tile">
      <div class="tile-head">Services &amp; Consulting</div>
      <div class="tile-img" role="img" aria-label="Question marks on a blue background" style="background:linear-gradient(135deg,#5f8fb0,#a9c6d8)"></div>
    </div>
  </div>
</section>

<section class="partners">
  <h2 class="section-title">Our Partner</h2>
  <div class="abs partner-row">
    <span class="partner"><i></i>Orvadex</span>
    <span class="partner"><i></i>Qalen</span>
    <span class="partner">Ardent</span>
    <span class="partner"><i class="round"></i>Brookvale</span>
    <span class="partner"><i class="round"></i>KR</span>
    <span class="partner"><i class="round"></i>Enmere</span>
    <span class="partner"><i></i>Holtby</span>
  </div>
</section>

<section class="abs info">
  <div class="col col-about">
    <h2>ABOUT US</h2>
    <p>From early phase evaluation through planning, execution and post analysis of wells, we deliver the tools, processes and people required to facilitate major performance improvement and cost savings.</p>
    <p>Our solutions are used in more than 30 countries to support operations ranging from a single well to global deployments with Major Operators.</p>
  </div>
  <div class="col col-news">
    <h2>LATEST NEWS</h2>
    <p><strong>PRV Selected by Brookvale</strong><br>Brookvale Energy Ltd has selected PRV as the solution to provide probabilistic time and cost estimates for its drilling operations.</p>
    <p style="margin-top:14px"><strong>LTM Implementation at Enmere</strong><br>Enmere selects LTM to support its materials, logistics &amp; cost management processes.</p>
  </div>
  <div class="col col-location">
    <h2>Location</h2>
    <p><strong>EUROPE</strong><br>18 Harlow Lane<br>Kelmouth<br>KM4 2RD<br>Phone:+44(0)1632 960418<br>Email: eu@corvanisystems.com</p>
    <p><strong>NORTH AMERICA</strong><br>1400 Birch Row Blvd<br>Suite 210<br>Marlton, TX 77510<br>Phone:(555) 014 2278<br>Email: us@corvanisystems.com</p>
  </div>
  <div class="continue" style="left:27px">Continue Reading..</div>
  <div class="continue" style="left:260px">Continue Reading..</div>
  <div class="continue" style="left:492px">Continue Reading..</div>
</section>

<div class="abs partner-badge"><b>Solvane Partner</b><small>Gold Independent Software Vendor (ISV)</small></div>
<div class="abs touch">
  <div class="touch-pill">Get In Touch
    <svg width="16" height="18" viewBox="0 0 16 18"><path d="M3 1l3 4-2 2c1 3 3 5 6 6l2-2 4 3-2 3C7 17 1 11 1 3z" fill="#fff"/></svg>
    <svg width="18" height="13" viewBox="0 0 18 13"><rect x="1" y="1" width="16" height="11" fill="none" stroke="#fff" stroke-width="2"/><path d="M1 1l8 6 8-6" fill="none" stroke="#fff" stroke-width="2"/></svg>
    <svg width="12" height="18" viewBox="0 0 12 18"><path d="M6 17C2 11 1 8 1 6a5 5 0 0110 0c0 2-1 5-5 11z" fill="none" stroke="#fff" stroke-width="2"/><circle cx="6" cy="6" r="2" fill="#fff"/></svg>
  </div>
</div>

<form class="abs contact-form">
  <div class="field" style="left:20px;top:21px;width:150px">First Name</div>
  <div class="field" style="left:178px;top:21px;width:150px">Last Name</div>
  <div class="field" style="left:20px;top:45px;width:150px">Email</div>
  <div class="field" style="left:178px;top:45px;width:150px">Company</div>
  <div class="field" style="left:20px;top:69px;width:225px;height:34px">Message</div>
  <div class="send">SEND</div>
</form>

<ul class="abs footer-nav"><li>HOME</li><li>NEWS</li><li>ABOUT US</li><li>SOLUTIONS</li><li>CONTACT US</li></ul>
<p class="abs copyright">All rights reserved 2012 &nbsp; visit our website : www.corvanisystems.com</p>
<a class="abs social" style="left:745px" aria-label="Social link one"></a>
<a class="abs social" style="left:775px" aria-label="Social link two"></a>

<div class="abs bottom-strip"></div>
</body>
</html>
```